SilverLedgerOak - Double Sided Business Card

We are looking for design options or our business cards. We are a Business Solutions and HR solutions Provider - the theme is business, for this card.

Our brand colours are represented within our logo.

Details needed to be put on the front of the business card are:

Employees name: [Sample Name]
Role: [Sample Role]

Address: Suite 4 - Level 3/48 Halloran Avenue Parramatta NSW 2150
M: 0000 000 000
P: 1300 847 213
F: 1300 847 286
E: sample@silverledgeroak.com.au
www.silverledgeroak.com.au
Updates

Reason: Hello, could we please increase our deadline by 5 days. Thanking you, Tess

Target Market(s)

Business Owners, also Candidates looking for Employment

Industry/Entity Type

Business

Contact Information for Business Card

Role: [Sample Role]

M: 0000 000 000
P: 1300 847 213
F: 1300 847 286

Font styles to use
Sans Serif

Colors
3276b5
3176b5
0455a3
85abd2
cfdeed
ffffff
000000
1b1b1b
757575

Requirements
Must have
• Details needed to be put on the front of the business card are:
• Employees name: [Sample Name]
• Role: [Sample Role]
• Address: Suite 4 - Level 3/48 Halloran Avenue Parramatta NSW 2150
• M: 0000 000 000
• P: 1300 847 213
• F: 1300 847 286
• E: sample@silverledgeroak.com.au
• www.silverledgeroak.com.au
Nice to have
• Simplicity, clean and professional.

```html
<!DOCTYPE html>
<html lang="en">
<head>
<meta charset="utf-8">
<title>SilverLedgerOak Business Card</title>
<link rel="stylesheet" href="https://fonts.googleapis.com/css2?family=Open+Sans:wght@400;600;700&display=swap">
<style>
  :root {
    --navy: #0d2340;
    --royal: #0a56a8;
    --brand: #0455a3;
    --ink: #1b1b1b;
    --grey: #757575;
    --paper: #ffffff;
    --paper-shade: #f1f2f4;
    --stage: #6b6e72;
  }
  * { margin: 0; padding: 0; box-sizing: border-box; }
  html, body { width: 1200px; height: 904px; overflow: hidden; }
  body {
    background: var(--stage);
    font-family: "Open Sans", Arial, sans-serif;
    position: relative;
  }
  .card {
    position: absolute;
    width: 620px;
    height: 379px;
    overflow: hidden;
    box-shadow: 0 10px 28px rgba(0,0,0,.35);
  }
  .card-back { left: 140px; top: 50px; background: var(--navy); }
  .card-back svg { position: absolute; inset: 0; }
  .back-brand {
    position: absolute;
    left: 0; right: 0; top: 168px;
    display: flex; justify-content: center; align-items: center; gap: 12px;
    color: var(--paper);
    font-weight: 700;
    font-size: 30px;
    letter-spacing: .5px;
  }
  .back-brand .mark { width: 20px; height: 20px; background: var(--paper); }

  .card-front {
    left: 440px; top: 475px;
    background: linear-gradient(120deg, var(--paper) 0%, var(--paper-shade) 100%);
  }
  .front-brand {
    position: absolute; left: 56px; top: 52px;
  }
  .brand-name {
    display: flex; align-items: center; gap: 10px;
    color: var(--brand); font-weight: 700; font-size: 26px; letter-spacing: .3px;
  }
  .brand-name .mark { width: 16px; height: 16px; background: var(--brand); }
  .tagline {
    margin-top: 4px; padding-top: 3px;
    border-top: 1px solid var(--brand);
    font-size: 9px; font-weight: 700; color: var(--ink);
  }
  .address {
    position: absolute; left: 56px; top: 140px;
    font-size: 15px; line-height: 1.35; color: var(--grey);
  }
  .contacts {
    position: absolute; left: 56px; top: 222px;
    list-style: none; font-size: 15px; color: var(--grey);
  }
  .contacts li { display: flex; align-items: center; gap: 12px; height: 23px; }
  .contacts svg { width: 14px; height: 14px; fill: var(--brand); flex: none; }
  .person {
    position: absolute; left: 380px; top: 92px;
  }
  .person-name { font-size: 18px; font-weight: 700; color: var(--navy); }
  .person-role { font-size: 14px; color: var(--grey); margin-left: 18px; }
  .edge-band {
    position: absolute; right: 0; top: 0; bottom: 0; width: 16px; background: var(--royal);
  }
</style>
</head>
<body>

<section class="card card-back" aria-label="Card back">
  <svg width="620" height="379" viewBox="0 0 620 379" aria-hidden="true">
    <polygon points="0,150 310,190 390,379 0,379" fill="var(--royal)"/>
  </svg>
  <div class="back-brand"><span class="mark"></span>SilverLedgerOak</div>
</section>

<section class="card card-front" aria-label="Card front">
  <div class="front-brand">
    <div class="brand-name"><span class="mark"></span>SilverLedgerOak</div>
    <p class="tagline">Helping small to medium business realise their potential</p>
  </div>

  <address class="address" style="font-style:normal">
    Suite 4 - Level 3/48<br>Halloran Avenue<br>Parramatta NSW 2150
  </address>

  <ul class="contacts">
    <li><svg viewBox="0 0 14 14"><rect x="3" y="0" width="8" height="14" rx="1.5"/><rect x="4.5" y="2" width="5" height="8" fill="#fff"/></svg>0000 000 000</li>
    <li><svg viewBox="0 0 14 14"><path d="M3 1l3 3-1.5 1.5c.8 1.8 2.2 3.2 4 4L10 8l3 3-2 2C6 13 1 8 1 3z"/></svg>1300 847 213</li>
    <li><svg viewBox="0 0 14 14"><rect x="3" y="1" width="8" height="4"/><rect x="1" y="5" width="12" height="6" rx="1"/><rect x="3" y="9" width="8" height="4" fill="#fff" stroke="var(--brand)"/></svg>1300 847 286</li>
    <li><svg viewBox="0 0 14 14"><rect x="0" y="2" width="14" height="10" rx="1"/><path d="M1 3l6 5 6-5" fill="none" stroke="#fff" stroke-width="1.4"/></svg>sample@silverledgeroak.com.au</li>
    <li><svg viewBox="0 0 14 14"><circle cx="7" cy="7" r="7"/><path d="M0 7h14M7 0v14M2.5 3.5h9M2.5 10.5h9" stroke="#fff" stroke-width="1" fill="none"/></svg>www.silverledgeroak.com.au</li>
  </ul>

  <div class="person">
    <p class="person-name">Alex Reed</p>
    <p class="person-role">Manager</p>
  </div>

  <div class="edge-band"></div>
</section>

</body>
</html>
```